Business Card Design Project

I need a business card design for our new logo, please check the logo at the following link:
https://www.filecrate.net/s/q7rtx2pw9kd41m/FernLoop.png
The address on the business card:
Av. Gervásio Tavares 418 sala 207
Barra da Tijuca, Rio de Janeiro, RJ
CEP: 22714-380
Brasil
Phone: +55 21 86347215
e-mail: osvaldo@fernloop.com.br
Updates
Thank you all for sending your designs, we will not provide feedback because there are too many designs, on December 3 we will pick the best design according to our point of view. Please keep posting.
Osvaldo
Industry/Entity Type
Business
Look and feel
Each slider illustrates characteristics of the customer's brand and the style your logo design should communicate.

```html
<!DOCTYPE html>
<html lang="pt-BR">
<head>
<meta charset="utf-8">
<title>FernLoop – Cartão de Visita</title>
<link rel="stylesheet" href="https://fonts.googleapis.com/css2?family=Kurale&display=swap">
<style>
  :root {
    --backdrop: #1f1f1f;
    --card: #ffffff;
    --ink: #2b2b2b;
    --brand-ink: #3a3022;
    --swoosh-dark: #2f3532;
    --swoosh-brown: #4d3a14;
    --icon-fill: #3fb3c6;
    --icon-ring: #1d7f91;
    --divider: #9aa79a;
  }
  html, body {
    margin: 0;
    padding: 0;
    width: 1200px;
    height: 900px;
    overflow: hidden;
    background: var(--backdrop);
  }
  .canvas {
    position: relative;
    width: 1200px;
    height: 900px;
  }
  .business-card {
    position: absolute;
    left: 150px;
    top: 180px;
    width: 900px;
    height: 540px;
    background: var(--card);
    overflow: hidden;
    font-family: "Kurale", serif;
    color: var(--ink);
  }
  .card-swooshes {
    position: absolute;
    inset: 0;
    width: 900px;
    height: 540px;
  }
  .brand-name {
    position: absolute;
    top: 62px;
    left: 0;
    width: 100%;
    margin: 0;
    text-align: center;
    font-size: 72px;
    font-weight: 400;
    line-height: 1;
    color: var(--brand-ink);
  }
  .contact-direct {
    position: absolute;
    right: 478px;
    top: 206px;
    display: flex;
    flex-direction: column;
    align-items: flex-end;
    gap: 12px;
    font-size: 19px;
  }
  .contact-line {
    display: flex;
    align-items: center;
    gap: 8px;
    white-space: nowrap;
  }
  .contact-icon {
    width: 24px;
    height: 24px;
    flex: none;
  }
  .divider {
    position: absolute;
    left: 440px;
    top: 175px;
    width: 2px;
    height: 135px;
    background: var(--divider);
  }
  .contact-address {
    position: absolute;
    left: 458px;
    top: 178px;
    display: flex;
    gap: 10px;
    font-size: 19px;
    line-height: 1.38;
  }
  .contact-address .contact-icon {
    margin-top: 2px;
  }
  .address-lines {
    margin: 0;
    font-style: normal;
    white-space: nowrap;
  }
  .address-lines span {
    display: block;
  }
  .address-lines .indent {
    padding-left: 22px;
  }
</style>
</head>
<body>
<main class="canvas">
  <section class="business-card" aria-label="Cartão de visita FernLoop">
    <svg class="card-swooshes" viewBox="0 0 900 540" aria-hidden="true">
      <path d="M0 250 Q 430 470 900 290" fill="none" stroke="var(--swoosh-dark)" stroke-width="11"/>
      <path d="M0 300 Q 420 560 900 360 L 900 385 Q 420 640 0 350 Z" fill="var(--swoosh-brown)"/>
    </svg>

    <h1 class="brand-name">FernLoop</h1>

    <div class="contact-direct">
      <div class="contact-line">
        <svg class="contact-icon" viewBox="0 0 26 26" aria-hidden="true">
          <circle cx="13" cy="13" r="12" fill="var(--icon-fill)" stroke="var(--icon-ring)" stroke-width="1.5"/>
          <rect x="9" y="6" width="8" height="14" rx="1.5" fill="#fff"/>
          <rect x="10.5" y="8" width="5" height="6" fill="var(--icon-fill)"/>
        </svg>
        <span>+55 21 86347215</span>
      </div>
      <div class="contact-line">
        <svg class="contact-icon" viewBox="0 0 26 26" aria-hidden="true">
          <circle cx="13" cy="13" r="12" fill="var(--icon-fill)" stroke="var(--icon-ring)" stroke-width="1.5"/>
          <rect x="6.5" y="8.5" width="13" height="9" fill="#fff"/>
          <path d="M6.5 8.5 L13 14 L19.5 8.5" fill="none" stroke="var(--icon-ring)" stroke-width="1.2"/>
        </svg>
        <span>osvaldo@fernloop.com.br</span>
      </div>
    </div>

    <div class="divider" aria-hidden="true"></div>

    <div class="contact-address">
      <svg class="contact-icon" viewBox="0 0 26 26" aria-hidden="true">
        <circle cx="13" cy="13" r="12" fill="var(--icon-fill)" stroke="var(--icon-ring)" stroke-width="1.5"/>
        <path d="M6 13 L13 6.5 L20 13" fill="none" stroke="#fff" stroke-width="2"/>
        <path d="M8.5 12 V19 H17.5 V12" fill="none" stroke="#fff" stroke-width="2"/>
      </svg>
      <address class="address-lines">
        <span>Av. Gervásio Tavares 418 sala 207</span>
        <span class="indent">Barra da Tijuca, Rio de Janeiro, RJ</span>
        <span class="indent">CEP: 22714-380</span>
        <span class="indent">Brasil</span>
      </address>
    </div>
  </section>
</main>
</body>
</html>
```